Parcelnook.com.au Front page Re-Design

We need a front page redesign for the website parcelnook.com.au,
The site needs to keep a number of products products highlighted on the front page. Same buttons but navigation could be different and we still need some text for SEO.
What we do not currently like:
1. The big banners.
2. The use of too much orange especially the 50% orange borders.
3. the fact that products cannot be seen straight away when logged-in.
4. The fact that it is hard to convert to tablet friendly
5. The fact that it's not a modern design.

What we think we want:

1. Maybe more use of 1 colour (purple or orange) with the other a secondary highlight colour.
2. A more modern look
3. The wow factor

Look at parcelnook.com.au take the elements that you need and design.
Updates

Reason: Designs are getting better. liking the designs that don't look like the usual e-commerce templates out there.

Hello,

We are making decisions next Monday. Sorry for the delay but there has been a lot of holidays in Australia and decision makers away.

Industry/Entity Type

Seo

Colors
6b449b
f78f20
ffffff

```html
<!DOCTYPE html>
<html lang="en">
<head>
<meta charset="utf-8">
<title>Parcelnook.com.au – Gifts &amp; Hampers Delivered</title>
<link href="https://fonts.googleapis.com/css2?family=Open+Sans:wght@300;400;600;700&display=swap" rel="stylesheet">
<style>
:root{
  --purple:#8e2a8b;
  --purple-dark:#6b449b;
  --orange:#f7941d;
  --teal:#2a98b8;
  --pink:#f06fb0;
  --ink:#222;
  --muted:#555;
  --line:#d6d6d6;
  --page:#f6f6f6;
  --white:#fff;
}
*{box-sizing:border-box;margin:0;padding:0}
html,body{width:1200px;height:1000px;overflow:hidden}
body{font-family:'Open Sans',sans-serif;background:var(--page);color:var(--ink);position:relative}
.abs{position:absolute}
/* top bar */
.topbar{left:0;top:0;width:1200px;height:33px;background:var(--purple);color:var(--white);font-size:14px}
.topbar .item{position:absolute;top:7px;display:flex;align-items:center;gap:7px}
.topbar svg{fill:var(--white)}
.search{position:absolute;left:980px;top:6px;width:145px;height:21px;background:var(--white)}
.search svg{position:absolute;right:6px;top:3px}
/* header */
.header{left:0;top:33px;width:1200px;height:104px;background:var(--white);border-bottom:1px solid var(--line)}
.brand{position:absolute;left:62px;top:37px;display:flex;align-items:center;gap:10px}
.brand .mark{width:30px;height:30px;background:var(--orange)}
.brand .name{font-size:24px;font-weight:700;color:var(--purple);letter-spacing:-0.3px}
.perk{position:absolute;top:36px;display:flex;align-items:center;gap:8px}
.perk .t{color:var(--pink);font-weight:700;font-size:15px;line-height:16px;text-align:center}
.perk .s{font-size:10px;color:#333;display:block;font-weight:400}
.social{position:absolute;left:938px;top:38px;display:flex;gap:7px}
.social span{width:32px;height:32px;border-radius:50%;background:#333;display:block}
/* nav */
.nav{left:0;top:138px;width:1200px;height:35px;background:var(--white);border-bottom:1px solid var(--line)}
.nav ul{list-style:none;display:flex;gap:21px;position:absolute;left:61px;top:8px;font-size:14px;letter-spacing:-0.4px;color:#222}
.nav li.active{color:var(--purple)}
/* banner */
.banner{left:61px;top:196px;width:1064px;height:75px;background:var(--orange);color:var(--white);text-align:center}
.banner h1{font-weight:300;font-size:28px;line-height:30px;padding-top:10px}
.banner h1 b{font-weight:700}
.banner p{font-size:18px;font-weight:300;line-height:26px;margin-top:2px}
.banner p b{font-weight:700}
/* sidebar */
.side{left:61px;width:249px}
.side h2{font-weight:400;font-size:19px;color:var(--purple);border-bottom:1px solid #aaa;position:relative;height:28px}
.side h2 span{display:inline-block;border-bottom:2px solid var(--purple);height:28px}
.side h2:after{content:"";position:absolute;right:20px;top:9px;width:6px;height:6px;border-right:1.5px solid #999;border-bottom:1.5px solid #999;transform:rotate(45deg)}
.side ul{list-style:none;padding:28px 0 0 20px}
.side li{font-size:14px;color:#444;height:31px;position:relative}
.side li:after{content:"";position:absolute;right:20px;top:7px;width:5px;height:5px;border-right:1.5px solid #999;border-top:1.5px solid #999;transform:rotate(45deg)}
/* category cards */
.cat{top:308px;width:249px;height:356px;background:var(--white);border:1px solid}
.cat .img{height:291px}
.cat .label{height:64px;color:var(--white);text-align:center;font-size:25px;line-height:28px;padding-top:8px}
.cat .label small{display:block;font-size:13px;line-height:16px}
.cat.him{border-color:var(--teal)} .cat.him .label{background:var(--teal)}
.cat.her{border-color:var(--purple)} .cat.her .label{background:var(--purple)}
.cat.kids{border-color:var(--orange)} .cat.kids .label{background:var(--orange)}
/* top products */
.section-title{font-size:19px;font-weight:400;color:var(--purple);border-bottom:1px solid #888;height:28px}
.arrows{position:absolute;right:0;top:2px;display:flex;gap:4px}
.product{top:760px;height:250px;background:var(--white);border:1px solid #e6c9e5;text-align:center}
.product.first{border-color:var(--purple)}
.product .img{height:160px;margin:6px}
.product .name{font-size:11px;font-weight:700;color:#333;line-height:13px;margin-top:8px;height:28px}
.product.first .name{color:var(--purple)}
.product .price{font-size:20px;margin-top:-2px}
/* right column */
.info h3{font-size:16px;font-weight:700;color:#111;line-height:18px}
.info p{font-size:15px;color:#111;line-height:17px}
.promo{left:877px;top:878px;width:248px;height:58px;background:var(--teal);color:var(--white);padding:6px 14px}
.promo b{display:block;font-size:20px;line-height:24px}
.promo span{font-size:16px}
.sendto{left:877px;top:955px;width:249px;height:43px;border:1px solid #ccc;background:#f0f0f0;font-size:14px;padding:11px 10px;display:flex;gap:8px;align-items:center}
</style>
</head>
<body>

<div class="abs topbar">
  <div class="item" style="left:480px"><svg width="12" height="13" viewBox="0 0 12 13"><circle cx="6" cy="3.5" r="3.2"/><path d="M0 13c0-4 2.5-6 6-6s6 2 6 6z"/></svg>Login<svg width="12" height="8" viewBox="0 0 12 8"><path d="M1 1l5 5 5-5" fill="none" stroke="#fff" stroke-width="1.5"/></svg></div>
  <div class="item" style="left:622px"><svg width="14" height="12" viewBox="0 0 14 12"><path d="M7 12L1 6A3.2 3.2 0 017 1.6 3.2 3.2 0 0113 6z"/></svg>Wishlist (0)</div>
  <div class="item" style="left:775px"><svg width="14" height="12" viewBox="0 0 14 12"><path d="M0 1h3l2 7h7l2-5H4.5"/><circle cx="6" cy="10.5" r="1.3"/><circle cx="11" cy="10.5" r="1.3"/></svg>Shopping cart (0): $0.00</div>
  <div class="search"><svg width="14" height="14" viewBox="0 0 14 14"><circle cx="6" cy="6" r="4.5" fill="none" stroke="#bbb" stroke-width="1.6"/><path d="M9.5 9.5l3.5 3.5" stroke="#bbb" stroke-width="1.8"/></svg></div>
</div>

<header class="abs header">
  <div class="brand"><span class="mark"></span><span class="name">parcelnook.com.au</span></div>
  <div class="perk" style="left:603px">
    <svg width="24" height="28" viewBox="0 0 24 28"><rect x="1" y="1" width="22" height="21" rx="4" fill="#444"/><rect x="4" y="5" width="16" height="7" fill="#fff"/><circle cx="6" cy="17" r="2" fill="#fff"/><circle cx="18" cy="17" r="2" fill="#fff"/><rect x="3" y="22" width="4" height="5" fill="#444"/><rect x="17" y="22" width="4" height="5" fill="#444"/></svg>
    <div class="t">FREE SHIPPING<span class="s">on all orders over 50$</span></div>
  </div>
  <div class="perk" style="left:765px">
    <svg width="27" height="27" viewBox="0 0 27 27"><circle cx="13.5" cy="13.5" r="12" fill="none" stroke="#444" stroke-width="2"/><path d="M13.5 6v8h5" fill="none" stroke="#444" stroke-width="2"/></svg>
    <div class="t">NEXT DAY<span class="s">dispatch</span></div>
  </div>
  <div class="social"><span></span><span></span><span></span><span></span><span></span></div>
</header>

<nav class="abs nav">
  <ul>
    <li class="active">HOME</li><li>EASTER</li><li>MOTHERS DAY</li><li>GET WELL</li><li>THANK YOU</li><li>BIRTHDAY</li><li>ANNIVERSARY</li><li>ROMANCE</li><li>NEW BABY</li><li>CHILDRENS</li><li>FOR HIM</li><li>FOR HER</li>
  </ul>
</nav>

<section class="abs banner">
  <h1>Looking for <b>Something Special?</b></h1>
  <p>Simply call customer support on: <b>+61 1300 555 018</b> FOR FURTHER INFORMATION</p>
</section>

<aside>
  <div class="abs side" style="top:300px">
    <h2><span>Shop By Basket Price</span></h2>
    <ul><li>Gift Under $50</li><li>Gift $50 to $75</li><li>Gift $75 to $100</li><li>Gift $100 to $150</li><li>Gift Over $150</li></ul>
  </div>
  <div class="abs side" style="top:523px">
    <h2><span>Shop By Basket Style</span></h2>
    <ul><li>Chocolate Bouquets</li><li>Plant Gifts</li><li>Fruit Hampers</li><li>Pamper Packs</li><li>Lollies &amp; Sweets</li><li>Teddy Bears &amp; Toys</li><li>Gourmet Hampers</li><li>Champagne &amp; Liquor</li><li>Personalised Items</li><li>Corporate Gifts</li></ul>
  </div>
  <div class="abs side" style="top:903px">
    <h2><span>Shop By Occasions</span></h2>
    <ul><li>Easter Gifts</li><li>Mothers Day Gifts</li></ul>
  </div>
</aside>

<div class="abs cat him" style="left:332px">
  <div class="img" role="img" aria-label="Teddy bear with a bottle of whisky in a wooden crate" style="background:linear-gradient(160deg,#fff 10%,#c79a6a 55%,#8a6540)"></div>
  <div class="label">For Him<small>10 Items</small></div>
</div>
<div class="abs cat her" style="left:604px">
  <div class="img" role="img" aria-label="Pamper gift box with toiletries and red ribbon" style="background:linear-gradient(170deg,#fff 10%,#d33 45%,#333 80%)"></div>
  <div class="label">For Her<small>10 Items</small></div>
</div>
<div class="abs cat kids" style="left:876px">
  <div class="img" role="img" aria-label="Two plush owl toys on a wooden crate" style="background:linear-gradient(100deg,#fff 5%,#3bb2e6 35%,#8a4fb0 70%,#fff 95%)"></div>
  <div class="label">Children<small>10 Items</small></div>
</div>

<div class="abs" style="left:332px;top:715px;width:519px">
  <h2 class="section-title">Todays Top Products</h2>
  <div class="arrows">
    <svg width="19" height="19" viewBox="0 0 19 19"><circle cx="9.5" cy="9.5" r="8.5" fill="none" stroke="#222" stroke-width="1.5"/><path d="M11 5l-4 4.5 4 4.5z" fill="#222"/></svg>
    <svg width="19" height="19" viewBox="0 0 19 19"><circle cx="9.5" cy="9.5" r="8.5" fill="none" stroke="#222" stroke-width="1.5"/><path d="M8 5l4 4.5-4 4.5z" fill="#222"/></svg>
  </div>
</div>

<div class="abs product first" style="left:332px;width:168px">
  <div class="img" role="img" aria-label="Easter bucket with chocolate eggs and bunny" style="background:radial-gradient(circle at 50% 55%,#7ac143,#a77dc9 55%,#fff 80%)"></div>
  <div class="name">Hollowbrook Chardonnay &amp;<br>Shiraz Double Gift</div>
  <div class="price">$39.00</div>
</div>
<div class="abs product" style="left:510px;width:167px">
  <div class="img" role="img" aria-label="Gift chest with wine and gourmet jars" style="background:radial-gradient(circle at 50% 50%,#5a2d6e,#c9a27a 55%,#fff 80%)"></div>
  <div class="name">Crumb And Rind<br>Gift Chest</div>
  <div class="price">$89.95</div>
</div>
<div class="abs product" style="left:685px;width:167px">
  <div class="img" role="img" aria-label="Basket of fresh mixed fruit" style="background:radial-gradient(circle at 50% 55%,#d63a2f,#9cc23b 45%,#f2c14e 65%,#fff 82%)"></div>
  <div class="name">Fruity Goodness</div>
  <div class="price">$70.00</div>
</div>

<div class="abs" style="left:877px;top:710px;width:249px">
  <h2 class="section-title" style="color:var(--pink)">Find out more Product</h2>
</div>
<div class="abs info" style="left:877px;top:754px;width:170px">
  <h3>First time here?</h3>
  <p>For further details about us and our current specials smply clck here</p>
</div>
<div class="abs" role="img" aria-label="Gift box with pointing hand" style="left:1050px;top:755px;width:62px;height:84px;background:linear-gradient(160deg,#f7941d,#8e2a8b)"></div>

<div class="abs promo">
  <b>Mother’s Day</b><span>Special Gift Products</span>
  <svg style="position:absolute;right:14px;top:15px" width="28" height="28" viewBox="0 0 28 28"><rect x="2" y="8" width="24" height="6" fill="#111"/><rect x="4" y="15" width="20" height="12" fill="#111"/><rect x="12.5" y="8" width="3" height="19" fill="#2a98b8"/><path d="M14 8C9 1 4 4 8 8M14 8c5-7 10-4 6 0" fill="none" stroke="#111" stroke-width="2"/></svg>
</div>
<div class="abs sendto">
  <svg width="16" height="16" viewBox="0 0 16 16"><circle cx="8" cy="8" r="7" fill="none" stroke="#444" stroke-width="1.3"/><path d="M8 4v8M4 8h8" stroke="#444" stroke-width="1.3"/></svg>
  Send Gifts to ...
</div>

</body>
</html>
```